QBoost480 Business Card Design

I am in need of a business card design.

Business Name: Quantum Boost 480 or Quantum Boost 480 (we can try the business card with both variations)

I would like it to be somewhat different from the "average" business card

What do we do?

We link up with distributors of different items and we Market their products, sell their products, fulfill the shipment, and handle all customer service that goes along with it.

I will be uploading our logo as well as other business card ideas that i have seen and liked on the web.

I like the style of the "graphic design" business card that i uploaded. I was thinking maybe something like that but instead would read.

SYNC | SELL | SHIP

With maybe:
a computer or a Sync icon underneath SYNC
Some form of money sign underneath Sell
a delivery truck or something underneath SHIP.

And then I was thinking maybe put the logo on the back side like in the other business card that i uploaded.

I definitely want a double sided business card.

These are only my suggestions and if i was very confident in my idea then I wouldn't have to be on here. (So make what you think is nice because my opinion is probably not so great anyway!!)

Everything can be changed.

ALSO, For the logo
We can try and remove the text multi channel selling

For the Business card contact info:
Milo Quenton
CEO
2914 Ravensby Street
J7T-2K8
Montreal, Quebec

Thanks

Target Market(s)

Businesses

Industry/Entity Type

Information Technology

Font styles to use
Serif
Sans Serif
Decorative

Colors
34a6d6
33b8a4
aaaaaa
85cae6
33a6d7
0492cd
9d9d9d

Requirements
Must have
• Double Sided Business card
Nice to have
• Illustration graphics / Icons underneath the main points

```html
<!DOCTYPE html>
<html lang="en">
<head>
<meta charset="utf-8">
<title>Quantum Boost 480 Business Card</title>
<link rel="stylesheet" href="https://fonts.googleapis.com/css2?family=Open+Sans:wght@700;800&family=Questrial&display=swap">
<style>
  :root {
    --backdrop: #ececec;
    --card: #ffffff;
    --green: #95c12b;
    --blue: #0aa0dc;
    --ink: #333333;
    --ink-soft: #3d3d3d;
    --white: #ffffff;
    --shadow: rgba(0, 0, 0, 0.18);
  }
  * { box-sizing: border-box; margin: 0; padding: 0; }
  html, body {
    width: 942px;
    height: 1200px;
    overflow: hidden;
    background: var(--backdrop);
  }
  .canvas {
    position: relative;
    width: 942px;
    height: 1200px;
  }
  .card {
    position: absolute;
    left: 93px;
    width: 745px;
    height: 451px;
    background: var(--card);
    box-shadow: 0 2px 6px var(--shadow);
    overflow: hidden;
  }
  .card--front { top: 106px; }
  .card--back { top: 637px; }
  .card__art {
    position: absolute;
    inset: 0;
    width: 745px;
    height: 451px;
  }

  /* Front */
  .brand-name {
    position: absolute;
    left: 44px;
    top: 176px;
    width: 250px;
    font-family: "Open Sans", sans-serif;
    font-weight: 800;
    font-size: 44px;
    line-height: 48px;
    letter-spacing: -0.5px;
    color: var(--ink);
  }
  .person__name {
    position: absolute;
    left: 380px;
    top: 50px;
    font-family: "Open Sans", sans-serif;
    font-weight: 700;
    font-size: 25px;
    line-height: 30px;
    color: var(--ink);
  }
  .person__role {
    position: absolute;
    left: 372px;
    top: 89px;
    font-family: "Questrial", sans-serif;
    font-size: 27px;
    line-height: 32px;
    color: var(--ink-soft);
  }
  .contact-list {
    position: absolute;
    left: 372px;
    top: 135px;
    list-style: none;
    font-family: "Questrial", sans-serif;
    font-size: 23px;
    line-height: 34px;
    color: var(--ink-soft);
  }
  .contact-list li {
    display: flex;
    align-items: center;
    gap: 6px;
    height: 34px;
  }
  .contact-list svg { width: 20px; height: 20px; flex: none; }
  .address {
    position: absolute;
    left: 372px;
    top: 270px;
    display: flex;
    gap: 6px;
    font-family: "Questrial", sans-serif;
    font-size: 23px;
    line-height: 29px;
    color: var(--ink-soft);
  }
  .address address { font-style: normal; }
  .address svg { width: 20px; height: 26px; flex: none; margin-top: 2px; }

  /* Back */
  .service {
    position: absolute;
    top: 150px;
    width: 120px;
    margin-left: -60px;
    text-align: center;
  }
  .service--sync { left: 212px; }
  .service--sell { left: 366px; }
  .service--ship { left: 528px; }
  .service__label {
    font-family: "Open Sans", sans-serif;
    font-weight: 700;
    font-size: 25px;
    line-height: 32px;
    color: var(--ink);
    letter-spacing: 0.5px;
  }
  .service__icon {
    display: block;
    width: 84px;
    height: 84px;
    margin: 6px auto 0;
  }
</style>
</head>
<body>
<main class="canvas">

  <section class="card card--front" aria-label="Business card front">
    <svg class="card__art" viewBox="0 0 745 451" aria-hidden="true">
      <defs>
        <clipPath id="front-stripe-band">
          <polygon points="741,0 745,0 745,451 692,451"/>
        </clipPath>
      </defs>
      <polygon points="353,0 741,0 692,451 303,451" fill="var(--green)"/>
      <g clip-path="url(#front-stripe-band)" fill="var(--blue)">
        <rect x="680" y="0" width="70" height="20"/>
        <rect x="680" y="39" width="70" height="34"/>
        <rect x="680" y="109" width="70" height="50"/>
        <rect x="680" y="181" width="70" height="50"/>
        <rect x="680" y="253" width="70" height="50"/>
        <rect x="680" y="325" width="70" height="49"/>
        <rect x="680" y="396" width="70" height="55"/>
      </g>
    </svg>

    <div class="brand-name">Quantum<br>Boost 480</div>

    <div class="person__name">Milo Quenton</div>
    <div class="person__role">CEO</div>

    <ul class="contact-list">
      <li>
        <svg viewBox="0 0 20 20" aria-hidden="true"><rect x="5" y="2" width="10" height="16" rx="1.5" fill="none" stroke="var(--ink)" stroke-width="1.6"/><line x1="5" y1="14.5" x2="15" y2="14.5" stroke="var(--ink)" stroke-width="1.2"/></svg>
        <span>555-214-9036</span>
      </li>
      <li>
        <svg viewBox="0 0 20 20" aria-hidden="true"><rect x="2" y="5" width="16" height="11" fill="none" stroke="var(--ink)" stroke-width="1.6"/><polyline points="2,5 10,11.5 18,5" fill="none" stroke="var(--ink)" stroke-width="1.6"/></svg>
        <span>hello@qboostcards.com</span>
      </li>
      <li>
        <svg viewBox="0 0 20 20" aria-hidden="true" fill="none" stroke="var(--ink)" stroke-width="1.4"><circle cx="10" cy="10" r="8"/><ellipse cx="10" cy="10" rx="3.5" ry="8"/><line x1="2" y1="10" x2="18" y2="10"/><line x1="3.5" y1="6" x2="16.5" y2="6"/><line x1="3.5" y1="14" x2="16.5" y2="14"/></svg>
        <span>www.qboostcards.com</span>
      </li>
    </ul>

    <div class="address">
      <svg viewBox="0 0 20 26" aria-hidden="true"><path d="M10 1a8 8 0 0 0-8 8c0 6 8 16 8 16s8-10 8-16a8 8 0 0 0-8-8z" fill="var(--ink)"/><circle cx="10" cy="9" r="3.2" fill="var(--green)"/></svg>
      <address>
        2914 Ravensby Street<br>
        J7T-2K8<br>
        Montreal, Quebec
      </address>
    </div>
  </section>

  <section class="card card--back" aria-label="Business card back">
    <svg class="card__art" viewBox="0 0 745 451" aria-hidden="true">
      <defs>
        <clipPath id="back-stripe-band">
          <polygon points="733,0 745,0 745,451 682,451"/>
        </clipPath>
      </defs>
      <g clip-path="url(#back-stripe-band)" fill="var(--green)">
        <rect x="670" y="0" width="80" height="15"/>
        <rect x="670" y="37" width="80" height="49"/>
        <rect x="670" y="108" width="80" height="50"/>
        <rect x="670" y="181" width="80" height="49"/>
        <rect x="670" y="252" width="80" height="50"/>
        <rect x="670" y="324" width="80" height="49"/>
        <rect x="670" y="395" width="80" height="56"/>
      </g>
    </svg>

    <div class="service service--sync">
      <div class="service__label">SYNC</div>
      <svg class="service__icon" viewBox="0 0 84 84" aria-hidden="true">
        <circle cx="42" cy="42" r="41" fill="var(--blue)"/>
        <rect x="20" y="25" width="44" height="28" rx="1.5" fill="var(--white)" stroke="#111" stroke-width="3"/>
        <rect x="39" y="53" width="6" height="7" fill="#111"/>
        <rect x="31" y="59" width="22" height="3.5" fill="#111"/>
      </svg>
    </div>

    <div class="service service--sell">
      <div class="service__label">SELL</div>
      <svg class="service__icon" viewBox="0 0 84 84" aria-hidden="true">
        <circle cx="42" cy="42" r="41" fill="var(--green)"/>
        <circle cx="42" cy="42" r="30" fill="var(--white)"/>
        <circle cx="42" cy="42" r="25" fill="var(--white)" stroke="#111" stroke-width="3"/>
        <text x="42" y="53" text-anchor="middle" font-family="Open Sans, sans-serif" font-weight="800" font-size="31" fill="#111">$</text>
      </svg>
    </div>

    <div class="service service--ship">
      <div class="service__label">SHIP</div>
      <svg class="service__icon" viewBox="0 0 84 84" aria-hidden="true">
        <circle cx="42" cy="42" r="41" fill="var(--blue)"/>
        <g fill="#111">
          <path d="M14 28h36v25H14z"/>
          <path d="M52 34h10l8 9v10H52z"/>
          <rect x="56" y="36.5" width="7" height="6" fill="var(--blue)"/>
          <circle cx="25" cy="55" r="5.5"/>
          <circle cx="60" cy="55" r="5.5"/>
        </g>
        <circle cx="25" cy="55" r="2.2" fill="var(--blue)"/>
        <circle cx="60" cy="55" r="2.2" fill="var(--blue)"/>
        <g stroke="var(--blue)" stroke-width="2">
          <line x1="34" y1="34" x2="48" y2="34"/>
          <line x1="38" y1="40" x2="48" y2="40"/>
          <line x1="42" y1="46" x2="48" y2="46"/>
        </g>
      </svg>
    </div>
  </section>

</main>
</body>
</html>
```